Label Design for RTD Cocktail Line Tolvanu Cellars

Tolvanu Cellars is a line of Indian-inspired artisan cocktails that "brings the bartender home" for professional men and women who like the finer things in life but don’t always have the time to treat themselves. No need for a multitude of expensive and hard-to-find ingredients, time consuming recipes, or a mixologist.

Our line of 3 open and serve cocktails blends a range of premium spirits with exotic ingredients so you can conveniently raise a glass for any of life’s celebrations.

Our bottle is the 750ml Claret bottle with Quorlex (screw cap) closure and will be covered entirely in a shrink sleeve (so potentially anything can be designed for any part of the bottle). We want the bottle to pop on the shelf so it should look different than what’s already out there (Velvet Fawn, Korvadel, Mirelda ready to drink cocktails). We are looking for a sexy design that's polished/sleek.
Updates

Reason: Hello designers! Tolvanu Cellars is so impressed with what we have received thus far and we would like to give some of the designers a few extra days to make the edits we requested. It's never too late to submit! Thank you all!

Requirements
Must have
• Front of bottle
* “Tolvanu Cellars” name and Peacock Logo- but feel free to pull the elements apart and use them on the bottle in different ways
* Open & Serve
* 12% ALC/VOL
* 750 ml
* 3 different labels in a theme for
-Brovanza
-Zestrovino
-Florquena

Brovanza Ideas- soft brown palate, the ingredients in chai spice (cloves, cardamom pods, nutmeg, black peppercorns, star anise, and cinnamon stick)

Zestrovino Ideas -cool and refreshing, pale green shade (not clashing with logo), graphics of fresh mint leaves, green chili, lime, cucumber

Florquena Ideas- soft/pale pink shades, graphics of lychi fruit (outer red shell and inner pink flesh), ginger

Back of bottle
* explanation of the 3 cocktails
Brovanza: Forget what you think you know about chai, this is not the Queen’s tea-time drink! Brovanza is a smooth, sweetly -spiced cocktail made with vodka, black tea, and a combination of aromatic spices. This velvety cocktail is rich without being heavy. Enjoy chilled or over ice anytime.

Zestrovino: Zestrovino can’t make up its mind! This fusion of zesty lime, sweet mint, earthy cucumber and spicy chilies is so refreshing you’ll crave it on a hot summer day or a cool winter’s night. The exotic botanicals in gin add a complexity to the cocktail making this a refreshing but potent drink! Enjoy chilled or over ice anytime.

Florquena: East meet West. Delicate lychi meet hard-hitting whiskey. Florquena will tempt you senses with flavor, fragrance and beauty. The peppery kick of ginger and the intensity of the un-aged whiskey are softened by lychi’s intoxicating scent and subtle, sweet finish.

Please include
1. Bottled By PQR Spirits Company
2. Sample barcode (where you would place it in your design)
3. www.TolvanuCellars.example
4. GOVERNMENT WARNING: (1) According to the Surgeon General, women should not drink alcoholic beverages during pregnancy because of the risk of birth defects. (2) Consumption of alcoholic beverages impairs your ability to drive a car or operate machinery, and may cause health problems.

Optional to include
*"Bring the Bartender Home"
*"Tolvanu Cellars” name and Peacock Logo on the back
*Entirely black sleeve with contrasting design

FYI the Fonts used in our logo are Geosans Light and Prakrta, but feel free to use other complimentary fonts on the other aspects.
Nice to have
• Optional to include

```html
<!DOCTYPE html>
<html lang="en">
<head>
<meta charset="utf-8">
<title>Tolvanu Cellars – RTD Cocktail Sleeves</title>
<link rel="stylesheet" href="https://fonts.googleapis.com/css2?family=Open+Sans:ital,wght@0,400;0,600;0,700;1,400&family=Playfair+Display:ital,wght@1,900&display=swap">
<style>
  :root {
    --canvas: #f2f1ee;
    --sleeve: #ffffff;
    --sleeve-edge: #dedcd6;
    --gold-light: #ecd9a0;
    --gold: #c9a85c;
    --gold-dark: #8f7434;
    --ink: #121212;
    --grey-text: #9a9a9a;
    --grey-strong: #7d7d7d;
    --ornament: #c8b59a;
    --brand: #1c7fa6;
    --spice: #7a4a26;
    --mint: #6ea832;
    --lime: #e2cf2a;
    --lychee: #c9304a;
    --lychee-flesh: #f0a6b8;
  }
  * { box-sizing: border-box; margin: 0; padding: 0; }
  html, body { width: 1200px; height: 1000px; overflow: hidden; }
  body {
    background: var(--canvas);
    font-family: "Open Sans", Arial, sans-serif;
    position: relative;
  }
  .bottle {
    position: absolute;
    top: 90px;
    width: 176px;
    height: 880px;
  }
  .bottle__shape { position: absolute; inset: 0; width: 176px; height: 880px; }
  .bottle__spec {
    position: absolute; left: 0; width: 100%;
    text-align: center; color: var(--grey-text);
    font-size: 10px; line-height: 1; white-space: nowrap;
  }
  .spec--abv { top: 362px; font-weight: 600; }
  .spec--enjoy { top: 380px; font-style: italic; }
  .spec--bottler { top: 398px; font-weight: 700; color: var(--grey-strong); font-size: 9.5px; }
  .bottle__serve {
    position: absolute; top: 424px; left: 0; width: 100%;
    text-align: center;
    font-size: 11px; font-weight: 600; color: var(--grey-strong);
  }
  .bottle__ornament {
    position: absolute; top: 470px; left: 8px; width: 160px; height: 280px;
    border-radius: 50% 50% 40% 40% / 60% 60% 30% 30%;
    background: radial-gradient(ellipse at 50% 55%, rgba(200,181,154,.75) 0%, rgba(200,181,154,.35) 45%, rgba(200,181,154,0) 72%);
  }
  .bottle__name {
    position: absolute; left: 112px; top: 610px; width: 320px;
    transform: translate(-50%, -50%) rotate(-90deg);
    text-align: center; white-space: nowrap;
    font-family: "Playfair Display", Georgia, serif;
    font-style: italic; font-weight: 900;
    font-size: 50px; line-height: 1; color: var(--ink);
  }
  .bottle__garnish {
    position: absolute; top: 778px; left: 100px; width: 42px; height: 46px;
    border-radius: 40%;
  }
  .garnish--spice { background: radial-gradient(circle at 40% 40%, #b07a4a, var(--spice) 70%); }
  .garnish--zest { background: radial-gradient(circle at 60% 55%, var(--lime) 0 30%, var(--mint) 60%); }
  .garnish--lychee { background: radial-gradient(circle at 60% 35%, var(--lychee-flesh) 0 28%, var(--lychee) 62%); }
  .bottle__volume {
    position: absolute; top: 790px; left: 30px;
    font-size: 10px; color: var(--grey-strong);
  }
  .bottle__brand {
    position: absolute; top: 830px; left: 0; width: 100%;
    display: flex; justify-content: center; align-items: center; gap: 5px;
    font-size: 14px; font-weight: 700; color: var(--brand); line-height: 1;
  }
  .brand__dot { width: 9px; height: 9px; border-radius: 50%; background: var(--brand); }
  .bottle__url {
    position: absolute; top: 852px; left: 0; width: 100%;
    text-align: center; font-size: 8.5px; font-weight: 700; color: var(--ink);
    white-space: nowrap;
  }
  .bottle--back .bottle__name { left: 58px; }
  .bottle--back .bottle__garnish { left: 38px; }
  .bottle--back .bottle__volume { left: 118px; }
  .bottle__warning {
    position: absolute; left: 140px; top: 610px; width: 330px;
    transform: translate(-50%, -50%) rotate(-90deg);
    font-size: 8.5px; line-height: 1.35; font-weight: 600; color: var(--grey-text);
  }
</style>
</head>
<body>
  <svg width="0" height="0" style="position:absolute" aria-hidden="true">
    <defs>
      <linearGradient id="cap-gold" x1="0" x2="1" y1="0" y2="0">
        <stop offset="0" stop-color="#8f7434"/>
        <stop offset=".35" stop-color="#ecd9a0"/>
        <stop offset=".6" stop-color="#c9a85c"/>
        <stop offset="1" stop-color="#8f7434"/>
      </linearGradient>
      <symbol id="bottle-silhouette" viewBox="0 0 176 880">
        <path d="M60,150 L60,195 C60,255 0,285 0,345 L0,860 Q0,878 18,878 L158,878 Q176,878 176,860 L176,345 C176,285 116,255 116,195 L116,150 Z"
              fill="#ffffff" stroke="#dedcd6" stroke-width="1.5"/>
        <rect x="58" y="0" width="60" height="155" rx="6" fill="url(#cap-gold)"/>
        <rect x="58" y="0" width="60" height="8" rx="4" fill="#8f7434" opacity=".5"/>
        <line x1="58" y1="62" x2="118" y2="62" stroke="#8f7434" stroke-width="1" opacity=".45"/>
      </symbol>
    </defs>
  </svg>

  <!-- Fronts -->
  <article class="bottle bottle--front" style="left:30px">
    <svg class="bottle__shape"><use href="#bottle-silhouette"/></svg>
    <p class="bottle__spec spec--abv">12% Alc / Vol</p>
    <p class="bottle__spec spec--enjoy">Enjoy responsibly</p>
    <p class="bottle__spec spec--bottler">Bottled By PQR Spirits Company</p>
    <p class="bottle__serve">Open &amp; Serve</p>
    <div class="bottle__ornament" role="img" aria-label="Gold paisley henna ornament"></div>
    <h2 class="bottle__name">Brovanza</h2>
    <div class="bottle__garnish garnish--spice" role="img" aria-label="Chai spices and a glass of spiced cocktail"></div>
    <p class="bottle__volume">750 ml</p>
    <div class="bottle__brand"><span class="brand__dot"></span>Tolvanu</div>
    <p class="bottle__url">www.TolvanuCellars.example</p>
  </article>

  <article class="bottle bottle--front" style="left:222px">
    <svg class="bottle__shape"><use href="#bottle-silhouette"/></svg>
    <p class="bottle__spec spec--abv">12% Alc / Vol</p>
    <p class="bottle__spec spec--enjoy">Enjoy responsibly</p>
    <p class="bottle__spec spec--bottler">Bottled By PQR Spirits Company</p>
    <div class="bottle__ornament" role="img" aria-label="Gold paisley henna ornament"></div>
    <h2 class="bottle__name">Zestrovino</h2>
    <div class="bottle__garnish garnish--zest" role="img" aria-label="Mint leaves, lime slice and green chili"></div>
    <p class="bottle__volume">750 ml</p>
    <div class="bottle__brand"><span class="brand__dot"></span>Tolvanu</div>
    <p class="bottle__url">www.TolvanuCellars.example</p>
  </article>

  <article class="bottle bottle--front" style="left:414px">
    <svg class="bottle__shape"><use href="#bottle-silhouette"/></svg>
    <p class="bottle__spec spec--abv">12% Alc / Vol</p>
    <p class="bottle__spec spec--enjoy">Enjoy responsibly</p>
    <p class="bottle__spec spec--bottler">Bottled By PQR Spirits Company</p>
    <div class="bottle__ornament" role="img" aria-label="Gold paisley henna ornament"></div>
    <h2 class="bottle__name">Florquena</h2>
    <div class="bottle__garnish garnish--lychee" role="img" aria-label="Lychee fruit and a pink cocktail glass"></div>
    <p class="bottle__volume">750 ml</p>
    <div class="bottle__brand"><span class="brand__dot"></span>Tolvanu</div>
    <p class="bottle__url">www.TolvanuCellars.example</p>
  </article>

  <!-- Backs -->
  <article class="bottle bottle--back" style="left:606px">
    <svg class="bottle__shape"><use href="#bottle-silhouette"/></svg>
    <p class="bottle__spec spec--abv">12% Alc / Vol</p>
    <p class="bottle__spec spec--enjoy">Enjoy responsibly</p>
    <p class="bottle__spec spec--bottler">Bottled By PQR Spirits Company</p>
    <h2 class="bottle__name">Brovanza</h2>
    <p class="bottle__warning">According to the Surgeon General, women should not drink alcoholic beverages during pregnancy because of the risk of birth defects. Consumption of alcoholic beverages impairs your ability to drive a car or operate machinery, and may cause health problems.</p>
    <div class="bottle__garnish garnish--spice" role="img" aria-label="Chai spices and a glass of spiced cocktail"></div>
    <p class="bottle__volume">750 ml</p>
    <div class="bottle__brand"><span class="brand__dot"></span>Tolvanu</div>
    <p class="bottle__url">www.TolvanuCellars.example</p>
  </article>

  <article class="bottle bottle--back" style="left:798px">
    <svg class="bottle__shape"><use href="#bottle-silhouette"/></svg>
    <p class="bottle__spec spec--abv">12% Alc / Vol</p>
    <p class="bottle__spec spec--enjoy">Enjoy responsibly</p>
    <p class="bottle__spec spec--bottler">Bottled By PQR Spirits Company</p>
    <h2 class="bottle__name">Zestrovino</h2>
    <p class="bottle__warning">According to the Surgeon General, women should not drink alcoholic beverages during pregnancy because of the risk of birth defects. Consumption of alcoholic beverages impairs your ability to drive a car or operate machinery, and may cause health problems.</p>
    <div class="bottle__garnish garnish--zest" role="img" aria-label="Mint leaves, lime slice and green chili"></div>
    <p class="bottle__volume">750 ml</p>
    <div class="bottle__brand"><span class="brand__dot"></span>Tolvanu</div>
    <p class="bottle__url">www.TolvanuCellars.example</p>
  </article>

  <article class="bottle bottle--back" style="left:990px">
    <svg class="bottle__shape"><use href="#bottle-silhouette"/></svg>
    <p class="bottle__spec spec--abv">12% Alc / Vol</p>
    <p class="bottle__spec spec--enjoy">Enjoy responsibly</p>
    <p class="bottle__spec spec--bottler">Bottled By PQR Spirits Company</p>
    <h2 class="bottle__name">Florquena</h2>
    <p class="bottle__warning">According to the Surgeon General, women should not drink alcoholic beverages during pregnancy because of the risk of birth defects. Consumption of alcoholic beverages impairs your ability to drive a car or operate machinery, and may cause health problems.</p>
    <div class="bottle__garnish garnish--lychee" role="img" aria-label="Lychee fruit and a pink cocktail glass"></div>
    <p class="bottle__volume">750 ml</p>
    <div class="bottle__brand"><span class="brand__dot"></span>Tolvanu</div>
    <p class="bottle__url">www.TolvanuCellars.example</p>
  </article>
</body>
</html>
```